CEREAL BOX DESIGN

I would like the box the same as the bag we created.

NOTE : the ingredients and warnings and such are all correct on the *mylar bag*. (The box file is out dated and most of the verbiage is incorrect). The only thing Id like from the former cereal box is the *game* on the back with the answers.

Please be sure to use the correct CMYK colors of course.

Must use the blank template provided for final design.

I was thinking of adding a cut out portion (like a purchase proof) for people to collect and save to earn gifts.

Requirements
Must have
• correct CMYK colors. All information from MylaR bag. Game.from fromer box file.

```html
<!DOCTYPE html>
<html lang="en">
<head>
<meta charset="utf-8">
<title>Sugar Haze – Frosted Strawberry Crunch Cereal Box Dieline</title>
<link href="https://fonts.googleapis.com/css2?family=Titan+One&family=Montserrat:wght@400;500;600&family=Tinos&display=swap" rel="stylesheet">
<style>
  :root {
    --box-pink: #e8a9ca;
    --cream-yellow: #f7f3a2;
    --white: #ffffff;
    --cut-line: #3a2a35;
    --fold-line: #86c06a;
    --dimension: #9c509f;
    --paper: #ffffff;
  }
  html, body { margin: 0; padding: 0; overflow: hidden; background: var(--paper); }
  .canvas { position: relative; width: 1200px; height: 1110px; overflow: hidden; background: var(--paper); }
  .dieline { position: absolute; left: 0; top: 0; }
  .txt { position: absolute; margin: 0; text-align: center; white-space: nowrap; }
  .display { font-family: "Titan One", sans-serif; line-height: 1; color: var(--white); text-shadow: 0 0 6px rgba(190, 90, 150, .35); }
  .display.yellow { color: var(--cream-yellow); }
  .brand { font-family: "Titan One", sans-serif; color: var(--cream-yellow); line-height: .95; }
  .spaced { font-family: "Montserrat", sans-serif; font-weight: 500; color: var(--white); letter-spacing: 3px; }
  .fine { font-family: "Montserrat", sans-serif; font-weight: 600; color: var(--white); font-size: 5.2px; line-height: 6.8px; text-align: left; white-space: normal; }
  .game { font-family: "Titan One", sans-serif; color: var(--white); }
  .dimension-label { font-family: "Tinos", serif; color: var(--dimension); line-height: 1; }
  .upside { transform: rotate(180deg); }
  .vertical { transform: rotate(-90deg); }

  /* front panel */
  .front-adult { left: 200px; top: 402px; width: 170px; font-size: 20px; }
  .front-thc { left: 200px; top: 424px; width: 170px; font-size: 56px; }
  .front-cereal { left: 170px; top: 476px; width: 230px; font-size: 58px; }
  .front-frosted { left: 150px; top: 570px; width: 280px; font-size: 55px; }
  .front-strawberry { left: 150px; top: 621px; width: 280px; font-size: 37px; }
  .front-crunch { left: 150px; top: 652px; width: 280px; font-size: 39px; }
  .front-descriptor { left: 150px; top: 703px; width: 280px; font-size: 12px; line-height: 15px; }
  .front-brand { left: 190px; top: 750px; width: 200px; font-size: 38px; }
  .front-warning { left: 150px; top: 835px; width: 280px; font-size: 11px; letter-spacing: 2.6px; }

  /* spine */
  .spine-frosted { left: 405px; top: 552px; width: 168px; height: 36px; font-size: 36px; }
  .spine-crunch { left: 376px; top: 558px; width: 282px; height: 26px; font-size: 23.5px; }
  .spine-brand { left: 454px; top: 765px; width: 96px; font-size: 26px; }

  /* back panel */
  .back-heading { left: 556px; top: 402px; width: 314px; font-size: 22px; line-height: 24px; }
  .scramble-title { left: 568px; top: 503px; width: 100px; font-size: 13px; }
  .scramble-list { left: 568px; top: 533px; width: 100px; font-size: 10px; letter-spacing: 4.5px; line-height: 19.6px; }
  .blank-title { left: 700px; top: 503px; width: 134px; font-size: 13px; line-height: 13.5px; }
  .blank-item { left: 680px; width: 174px; font-size: 9.5px; line-height: 11px; }
  .blank-line { display: inline-block; width: 38px; border-bottom: 1px solid var(--white); }
  .back-brand { left: 663px; top: 802px; width: 100px; font-size: 25px; }
  .back-check { left: 780px; top: 816px; width: 70px; font-size: 6.4px; line-height: 7.6px; white-space: normal; }
  .topflap-brand { left: 640px; top: 287px; width: 148px; font-size: 34px; }

  /* side panel */
  .side-ingredients { left: 881px; top: 405px; width: 90px; }
  .warning-box { position: absolute; left: 880px; top: 542px; width: 87px; height: 193px; border: 1.6px dotted var(--white); box-sizing: border-box; }
  .warning-inner { position: absolute; left: 885px; top: 545px; width: 80px; height: 187px; background: var(--white); }
  .warning-text { position: absolute; left: 888px; top: 550px; width: 75px; color: #111; font-family: "Montserrat", sans-serif; font-weight: 500; font-size: 5px; line-height: 6.6px; }
  .warning-text b { font-weight: 600; }
  .warning-pregnancy { margin-top: 4px; border: 1px solid #111; padding: 2px 2px 3px; }
  .side-made-in { left: 870px; top: 743px; width: 108px; text-align: center; }
  .side-brand { left: 870px; top: 763px; width: 108px; font-size: 24px; }
  .side-maker { left: 870px; top: 816px; width: 108px; text-align: center; }
  .side-url { left: 870px; top: 843px; width: 108px; text-align: center; }

  /* small flaps */
  .spine-flap-note { left: 460px; top: 320px; width: 90px; font-size: 5px; line-height: 7px; text-align: center; }
  .answer-fill { left: 140px; top: 920px; width: 84px; font-size: 5px; line-height: 7px; text-align: center; }
  .answer-brand { left: 231px; top: 906px; width: 100px; font-size: 24px; }
  .answer-scramble { left: 330px; top: 910px; width: 110px; font-size: 5px; line-height: 7px; text-align: center; }
</style>
</head>
<body>
<main class="canvas">

  <svg class="dieline" width="1200" height="1110" viewBox="0 0 1200 1110" aria-hidden="true">
    <g class="print-areas" fill="var(--box-pink)">
      <rect x="133" y="368" width="851" height="517"/>
      <polygon points="78,380 133,367 133,885 78,872"/>
      <polygon points="441,375 441,354 461,295 555,295 555,375"/>
      <path d="M550,375 V258 Q550,210 598,210 H828 Q876,210 876,258 V375 Z"/>
      <polygon points="870,375 870,295 960,295 973,350 984,362 984,375"/>
      <path d="M126,877 V995 Q126,1044 175,1044 H405 Q454,1044 454,995 V877 Z"/>
      <polygon points="448,877 448,957 543,957 555,900 561,894 561,877"/>
      <polygon points="864,877 864,890 873,900 880,957 984,957 984,877"/>
    </g>
    <g class="cut-lines" fill="none" stroke="var(--cut-line)" stroke-width=".8">
      <polyline points="133,375 85,384 85,868 133,877"/>
      <polyline points="448,375 448,356 463,303 549,303 556,375"/>
      <polyline points="557,375 557,267 575,267"/>
      <polyline points="851,267 869,267 869,375"/>
      <path d="M557,267 V240 Q557,218 585,218 H841 Q869,218 869,240 V267"/>
      <polyline points="870,375 877,303 958,303 970,352 978,360 978,375"/>
      <polyline points="133,877 133,984 153,984"/>
      <polyline points="428,984 447,984 447,877"/>
      <path d="M133,984 V1010 Q133,1036 160,1036 H420 Q447,1036 447,1010 V984"/>
      <polyline points="454,877 454,950 539,950 553,895 556,877"/>
      <polyline points="870,877 871,895 885,950 972,950 978,877"/>
    </g>
    <g class="fold-lines" fill="none" stroke="var(--fold-line)" stroke-width=".7">
      <line x1="133" y1="375" x2="978" y2="375"/>
      <line x1="133" y1="877" x2="978" y2="877"/>
      <line x1="133" y1="375" x2="133" y2="877"/>
      <line x1="448" y1="375" x2="448" y2="877"/>
      <line x1="556" y1="375" x2="556" y2="877"/>
      <line x1="870" y1="375" x2="870" y2="877"/>
      <line x1="575" y1="267" x2="851" y2="267"/>
      <line x1="153" y1="984" x2="428" y2="984"/>
    </g>
    <g class="dimensions" stroke="var(--dimension)" stroke-width=".8" fill="none">
      <line x1="447" y1="164" x2="870" y2="164"/>
      <line x1="447" y1="160" x2="447" y2="168"/>
      <line x1="555" y1="160" x2="555" y2="168"/>
      <line x1="870" y1="160" x2="870" y2="168"/>
      <line x1="1060" y1="374" x2="1060" y2="877"/>
      <line x1="1056" y1="374" x2="1064" y2="374"/>
      <line x1="1056" y1="877" x2="1064" y2="877"/>
    </g>
    <rect class="compliance-badge" x="376" y="400" width="48" height="48" rx="6" fill="var(--white)"/>
    <circle class="rewards-seal" cx="920" cy="339" r="29" fill="none" stroke="var(--white)" stroke-width="1.6"/>
  </svg>

  <p class="txt dimension-label" style="left:475px;top:120px;font-size:50px;">45</p>
  <p class="txt dimension-label" style="left:670px;top:120px;font-size:50px;">130</p>
  <p class="txt dimension-label vertical" style="left:1000px;top:600px;width:90px;font-size:50px;">209</p>

  <!-- front panel -->
  <p class="txt display front-adult">ADULT - USE</p>
  <p class="txt display front-thc">THC</p>
  <p class="txt display yellow front-cereal">CEREAL</p>
  <p class="txt display front-frosted">FROSTED</p>
  <p class="txt display front-strawberry">STRAWBERRY</p>
  <p class="txt display front-crunch">CRUNCH</p>
  <p class="txt spaced front-descriptor">FROSTED STRAWBERRY<br>CEREAL ENHANCED WITH THC</p>
  <p class="txt brand front-brand">SUGAR<br>HAZE</p>
  <p class="txt spaced front-warning">KEEP OUT OF REACH OF CHILDREN</p>

  <!-- spine -->
  <p class="txt display vertical spine-frosted">FROSTED</p>
  <p class="txt display vertical spine-crunch">STRAWBERRY CRUNCH</p>
  <p class="txt brand vertical spine-brand">SUGAR<br>HAZE</p>

  <!-- back top flap -->
  <p class="txt brand topflap-brand upside">SUGAR<br>HAZE</p>

  <!-- back panel: game -->
  <p class="txt display back-heading">WAKE UP WITH A<br>BOWL AND PLAY<br>A DOPE GAME</p>
  <p class="txt game scramble-title">SCRAMBLE</p>
  <p class="txt game scramble-list">EEFERR<br>JANGA<br>ONBG<br>DREIF<br>GHIH<br>CHONCIR<br>TNOSDE<br>IBOOBDE<br>HACRO<br>LRPOERL<br>BUTNL<br>PODE<br>ZLBAE<br>IZP<br>BDA<br>LLZIAS</p>
  <p class="txt game blank-title">FILL IN THE<br>BLANK</p>
  <p class="txt game blank-item" style="top:551px;">A FRIEND WITH <span class="blank-line"></span><br>IS A FRIEND INDEED.</p>
  <p class="txt game blank-item" style="top:595px;">IF WE ALL HAD A <span class="blank-line"></span><br>WE'D ALL GET ALONG.</p>
  <p class="txt game blank-item" style="top:639px;">STRUGGLE IS THE ENEMY<br><span class="blank-line"></span> IS THE REMEDY.</p>
  <p class="txt game blank-item" style="top:683px;">ALCOHOL KILLS , <span class="blank-line"></span> CHILLS.</p>
  <p class="txt game blank-item" style="top:716px;">INHALE THE <span class="blank-line"></span>,<br>EXHALE THE BULLSHIT.</p>
  <p class="txt game blank-item" style="top:761px;">KEEP <span class="blank-line"></span> ,<br>STAY AMAZING !</p>
  <p class="txt brand back-brand">SUGAR<br>HAZE</p>
  <p class="txt game back-check">CHECK YOUR ANSWERS ON THE BOTTOM</p>

  <!-- side panel -->
  <p class="txt fine side-ingredients">INGREDIENTS :<br>RICE, SUGAR, THC EXTRACT, COCONUT OIL, ARTIFICIAL FLAVOR &amp; COLOR, SALT, MALT SYRUP<br><br>ALLERGEN WARNING :<br>CONTAINS COCONUT. MADE IN A FACULTY THAT HANDLES PEANUTS AND OTHER TREE NUTS.<br><br>THE ACTUAL VALUE OF REPORTED CANNABINOIDS MAY VARY FROM THE REPORTED VALUE BY +/-10 %<br><br>ACTIVATION TIME :<br>10-60 MIN</p>
  <div class="warning-box"></div>
  <div class="warning-inner"></div>
  <div class="warning-text">
    <b>WARNING :</b><br>FOR USE BY INDIVIDUALS 21 YRS OF AGE OR OLDER OR BY REGISTERED QUALIFYING PATIENTS ONLY. IT IS ILLEGAL TO DRIVE A MOTOR VEHICLE WHILE UNDER THE INFLUENCE OF MARIJUANA. KEEP OUT OF REACH OF CHILDREN.<br><br>NATIONAL POISON CONTROL CENTER<br>1 800 555 0147
    <div class="warning-pregnancy"><b>WARNING :</b><br>USE BY PREGNANT OR BREASTFEEDING WOMEN OR BY WOMEN WHO PLAN TO BECOME PREGNANT MAY RESULT IN FETAL INJURY, PRETERM BIRTH, LOW BIRTHWEIGHT, OR DEVELOPMENTAL PROBLEMS FOR THE CHILD.</div>
  </div>
  <p class="txt fine side-made-in">MADE IN A<br>MARIJUANA FACILITY</p>
  <p class="txt brand side-brand">SUGAR<br>HAZE</p>
  <p class="txt fine side-maker">MADE &amp; DISTRIBUTED BY<br>MARLOW SNACK COMPANY<br>LICENSE # AU P 004817</p>
  <p class="txt fine side-url">www.SUGARHAZE.INFO</p>

  <!-- flaps -->
  <p class="txt fine spine-flap-note upside">VISIT<br>WWW.SUGARHAZE.INFO<br>TO TRADE YOUR<br>POINTS FOR<br>DOPE STUFF !</p>
  <p class="txt fine answer-fill upside">FILL IN THE BLANK :<br>1 WEED &nbsp;2 WEED<br>3 BONG &nbsp;4 WEED &nbsp;5 GOOD SHIT<br>6 BLAZING</p>
  <p class="txt brand answer-brand upside">SUGAR<br>HAZE</p>
  <p class="txt fine answer-scramble upside">SCRAMBLE :<br>1 REEFER &nbsp;2 GANJA &nbsp;3 BONG &nbsp;4 FRIED<br>5 HIGH &nbsp;6 CHRONIC &nbsp;7 STONED<br>8 DOOBIE &nbsp;9 ROACH &nbsp;10 PREROLL<br>11 BLUNT &nbsp;12 DOPE &nbsp;13 BLAZE<br>14 ZIP &nbsp;15 DAB &nbsp;16 ZILLAS</p>

</main>
</body>
</html>
```